Solvanta Clinica Business Card Design and print

I have attached the design I require including JPEG for company logo. I would like a copy of the art work for future needs.

Double sided - the item will not change from single

250 cards with both names on Ruth Calloway and Megan Thorpe

250 cards with Ruth Calloway only

Industry/Entity Type

Business

Contact Information for Business Card

See attached layout

```html
<!DOCTYPE html>
<html lang="en">
<head>
<meta charset="utf-8">
<title>Solvanta Clinica – Business Card</title>
<link rel="stylesheet" href="https://fonts.googleapis.com/css2?family=Quicksand:wght@400&family=Oswald:wght@600&family=Open+Sans:wght@400;600&display=swap">
<style>
  :root {
    --orange: #ec8a1a;
    --purple: #8c1fd0;
    --ink: #3a3a3a;
    --muted: #6a6a6a;
    --card: #ffffff;
    --backdrop: #e9e9ec;
  }
  * { box-sizing: border-box; margin: 0; padding: 0; }
  html, body { width: 1200px; height: 864px; overflow: hidden; }
  body {
    background: var(--backdrop);
    display: flex;
    flex-direction: column;
    align-items: center;
    justify-content: center;
    gap: 34px;
    font-family: "Open Sans", sans-serif;
  }
  .card {
    position: relative;
    width: 660px;
    height: 377px;
    background: var(--card);
    box-shadow: 0 6px 18px rgba(0,0,0,.15);
    overflow: hidden;
  }
  .brand {
    display: flex;
    align-items: center;
    gap: 14px;
    font-family: "Quicksand", sans-serif;
    font-weight: 400;
    color: var(--orange);
    line-height: 1;
  }
  .brand-mark {
    background: var(--purple);
    flex: none;
  }
  /* front */
  .card-front { display: flex; align-items: center; justify-content: center; }
  .card-front .brand { font-size: 50px; }
  .card-front .brand-mark { width: 66px; height: 66px; }
  /* back */
  .back-band { position: absolute; inset: 0; width: 100%; height: 100%; }
  .card-back .brand {
    position: absolute;
    right: 34px;
    top: 28px;
    flex-direction: column;
    align-items: flex-end;
    gap: 8px;
  }
  .card-back .brand-mark { width: 62px; height: 62px; margin-right: 58px; }
  .brand-name { text-align: right; font-size: 42px; line-height: 1.02; }
  .holder { position: absolute; left: 34px; top: 172px; }
  .holder-name {
    font-family: "Oswald", sans-serif;
    font-weight: 600;
    font-size: 22px;
    color: var(--orange);
    letter-spacing: .5px;
    text-transform: uppercase;
    line-height: 1.1;
  }
  .holder-role {
    font-size: 11px;
    font-weight: 600;
    color: var(--ink);
    letter-spacing: .6px;
    text-transform: uppercase;
  }
  .contacts { list-style: none; margin-top: 14px; }
  .contacts li {
    display: flex;
    align-items: center;
    gap: 8px;
    font-size: 10.5px;
    color: var(--muted);
    height: 17px;
  }
  .contacts svg { width: 11px; height: 11px; fill: var(--orange); flex: none; }
  .address {
    position: absolute;
    right: 30px;
    top: 282px;
    font-size: 15px;
    color: #fff;
    letter-spacing: .3px;
  }
</style>
</head>
<body>

<section class="card card-front" aria-label="Card front">
  <div class="brand">
    <span class="brand-mark"></span>
    <span class="brand-name-line">solvanta clinica</span>
  </div>
</section>

<section class="card card-back" aria-label="Card back">
  <svg class="back-band" viewBox="0 0 660 377" preserveAspectRatio="none" aria-hidden="true">
    <path fill="var(--purple)" d="M0 318 H250 C282 318 278 250 312 250 H660 V377 H0 Z"/>
    <path fill="var(--orange)" d="M0 328 H250 C282 328 278 260 312 260 H660 V377 H0 Z"/>
    <rect x="0" y="350" width="660" height="7" fill="var(--purple)"/>
  </svg>

  <div class="brand">
    <span class="brand-mark"></span>
    <span class="brand-name">solvanta<br>clinica</span>
  </div>

  <div class="holder">
    <p class="holder-name">Ruth Calloway</p>
    <p class="holder-role">General Manager</p>
    <ul class="contacts">
      <li><svg viewBox="0 0 12 12"><path d="M2.5 1h2l1 3-1.3 1a7 7 0 0 0 2.8 2.8l1-1.3 3 1v2a1.5 1.5 0 0 1-1.5 1.5A9.5 9.5 0 0 1 1 2.5 1.5 1.5 0 0 1 2.5 1z"/></svg>014 552 8130</li>
      <li><svg viewBox="0 0 12 12"><path d="M3.5 0h5a1 1 0 0 1 1 1v10a1 1 0 0 1-1 1h-5a1 1 0 0 1-1-1V1a1 1 0 0 1 1-1zm0 1.5v8h5v-8z"/></svg>014 552 8131</li>
      <li><svg viewBox="0 0 12 12"><path d="M1 2h10l-5 4zM1 3.5l5 4 5-4V10H1z"/></svg>014 552 8132</li>
      <li><svg viewBox="0 0 12 12"><path d="M0 2.5h12v7H0zM1 3.5l5 3.5 5-3.5" /></svg>ruth@solvantaclinica.com</li>
      <li><svg viewBox="0 0 12 12"><circle cx="6" cy="6" r="6"/></svg>www.solvantaclinica.com</li>
    </ul>
  </div>

  <p class="address">24 Harbor Lane, 2nd floor, Westgate</p>
</section>

</body>
</html>
```